(Grindstone Nook) sourcing coffee related material and services

we are a start up that provide all coffee related items for coffee shops and coffee fanatics. However, we mostly offer coffee machines customization that includes paint replacement and wood modification. we also focus on providing training for barista and coffee lovers.

we are looking for the following:

1-Design a logo that will be used for social media application and official paper work requirements

2- Design a business card (square shaped 2"*2") adopting the same logo and identity. please allow for adding mobile number, snapchat, and instgram accounts in the card.

3- Design a very basic monogram stamp by adding the three character (R4T) the number (2) shall be small in size just like how the numbers written in chemical formal.

Please take a quick look to instagram page to have a idea about the our start up

https://www.crumbleframe.example/grindstone_nook/

Target Market(s)

coffeeshop owners and coffee fanatics

Industry/Entity Type

Coffee Shop

Contact Information for Business Card

R4T
Grindstone Nook
editable text to add links to socail media

Logo Text

R4T

Font styles to use
Other font styles liked:
• flat design fonts

Colors

Designer to choose colors to be used in the design.

Requirements
Must have
• espresso portafilter, simple and minimal industrial look, wood,
Nice to have
• wood-making, portafilter, coffee beans, coffee tree,

```html
<!DOCTYPE html>
<html lang="en">
<head>
<meta charset="utf-8">
<title>R4T Grindstone Nook – Square Card</title>
<link href="https://fonts.googleapis.com/css2?family=Raleway:wght@300;400;800&display=swap" rel="stylesheet">
<style>
  :root {
    --page-bg: #e5e5e5;
    --wood-light: #f8d9a2;
    --wood-mid: #f3cf93;
    --ink-brown: #663300;
  }
  html, body {
    margin: 0;
    padding: 0;
    width: 1200px;
    height: 1200px;
    overflow: hidden;
    background: var(--page-bg);
    font-family: "Raleway", sans-serif;
    font-variant-numeric: lining-nums;
    font-feature-settings: "lnum" 1;
  }
  .card {
    position: absolute;
    left: 262px;
    top: 262px;
    width: 670px;
    height: 670px;
    background: linear-gradient(100deg, var(--wood-light), var(--wood-mid) 45%, var(--wood-light));
    color: var(--ink-brown);
  }
  .logo-frame {
    position: absolute;
    left: 70px;
    top: 100px;
    width: 530px;
    height: 270px;
    box-sizing: border-box;
    border: 5px solid var(--ink-brown);
    border-radius: 15px;
  }
  .logo-mark {
    position: absolute;
    left: 0;
    right: 0;
    top: 8px;
    text-align: center;
    font-weight: 800;
    font-size: 160px;
    line-height: 1;
    letter-spacing: 14px;
    padding-left: 14px;
  }
  .logo-name {
    position: absolute;
    left: 0;
    right: 0;
    top: 176px;
    text-align: center;
    font-weight: 300;
    font-size: 48px;
    line-height: 1;
    white-space: nowrap;
  }
  .social-list {
    position: absolute;
    left: 160px;
    top: 445px;
    margin: 0;
    padding: 0;
    list-style: none;
  }
  .social-item {
    display: flex;
    align-items: center;
    height: 54px;
    margin-bottom: 12px;
    font-size: 30px;
    font-weight: 400;
    white-space: nowrap;
  }
  .social-dot {
    width: 54px;
    height: 54px;
    border-radius: 50%;
    background: var(--ink-brown);
    margin-right: 20px;
    flex: none;
  }
</style>
</head>
<body>
  <div class="card">
    <div class="logo-frame">
      <div class="logo-mark">R4T</div>
      <div class="logo-name">GRINDSTONE NOOK</div>
    </div>
    <ul class="social-list">
      <li class="social-item"><span class="social-dot"></span>R4TGrindstone Nook</li>
      <li class="social-item"><span class="social-dot"></span>R4TGrindstone Nook</li>
      <li class="social-item"><span class="social-dot"></span>R4TGrindstone Nook</li>
    </ul>
  </div>
</body>
</html>
```